Beekeeper needs a label for honey jars

Ciao! I'm from Como Italy
I'm a hobbyist beekeeper and I produce honey for myself and my friends.
I've named my apiary "Dado di sole," a play on words between my nickname (Dado, from Edoardo) and the Italian expression "Dado di sole," which translates to "a drizzle of honey" in English.
I need to create a label for my honey glass jars (250 gr and 500 gr).
I don't need a label for commercial purposes. I would like to include at least the name “Apicoltura Dado di sole", the type of honey (e.g., wildflower, acacia...) and a space for the production year, to be handwritten each year.
In the design some references to the world of bees.
For reference, attached a label with a style I like
Attached are the images of the selected jars and their measurements
Thanks and good job!

beekeeping, honey

• I would like an elegant style with clean graphics.
• Predominance of black color.

```html
<!DOCTYPE html>
<html lang="it">
<head>
<meta charset="utf-8">
<title>Apicoltura Dado di sole – Honey Jar Label</title>
<link href="https://fonts.googleapis.com/css2?family=Montserrat:wght@300;400;600;800;900&display=swap" rel="stylesheet">
<style>
  :root {
    --page-bg: #f5f5f5;
    --label-black: #121512;
    --gold-light: #e8c177;
    --gold-mid: #b8995a;
    --gold-dark: #6e5a32;
    --white: #ffffff;
    --flag-green: #1f9a3a;
    --flag-white: #f2f2f2;
    --flag-red: #c8102e;
  }
  html, body {
    margin: 0;
    padding: 0;
    width: 1200px;
    height: 1200px;
    overflow: hidden;
    background: var(--page-bg);
  }
  .canvas {
    position: relative;
    width: 1200px;
    height: 1200px;
  }
  .label {
    position: absolute;
    left: 60px;
    top: 240px;
    width: 1080px;
    height: 720px;
    display: block;
  }
  .label-ground { fill: var(--label-black); }
  .label-text { font-family: 'Montserrat', sans-serif; text-anchor: middle; }
  .apiary-kicker { fill: var(--white); font-weight: 400; font-size: 30px; letter-spacing: 13px; }
  .brand-name { fill: url(#goldText); font-weight: 900; font-size: 70px; letter-spacing: 2px; }
  .honey-type { fill: var(--white); font-weight: 800; font-size: 30px; letter-spacing: 9px; }
  .year-caption { fill: var(--white); font-weight: 600; font-size: 13px; letter-spacing: 8px; }
  .year-box { fill: none; stroke: var(--gold-mid); stroke-width: 2; }
  .flag-green { fill: var(--flag-green); }
  .flag-white { fill: var(--flag-white); }
  .flag-red { fill: var(--flag-red); }
</style>
</head>
<body>
<div class="canvas">
  <svg class="label" viewBox="0 0 1222 815" xmlns="http://www.w3.org/2000/svg">
    <defs>
      <linearGradient id="goldField" x1="0" y1="0" x2="1" y2="0">
        <stop offset="0" stop-color="var(--gold-dark)"/>
        <stop offset="0.45" stop-color="var(--gold-light)"/>
        <stop offset="1" stop-color="var(--gold-dark)"/>
      </linearGradient>
      <linearGradient id="goldText" x1="0" y1="0" x2="0" y2="1">
        <stop offset="0" stop-color="var(--gold-light)"/>
        <stop offset="1" stop-color="var(--gold-dark)"/>
      </linearGradient>
    </defs>

    <rect class="label-ground" width="1222" height="815"/>

    <g role="img" aria-label="Gold honeycomb cluster decoration, top left">
      <polygon fill="url(#goldField)" points="0,0 595,0 560,58 480,90 420,150 330,150 300,210 260,240 215,270 160,270 105,210 55,180 40,120 0,120"/>
    </g>
    <g role="img" aria-label="Gold honeycomb cluster decoration, bottom right">
      <polygon fill="url(#goldField)" points="1222,815 628,815 660,760 735,725 800,665 885,665 915,600 960,570 1030,545 1100,580 1150,620 1170,700 1222,700"/>
    </g>

    <g role="img" aria-label="Gold bee illustration">
      <ellipse cx="610" cy="172" rx="42" ry="36" fill="var(--gold-mid)"/>
    </g>

    <text class="label-text apiary-kicker" x="614" y="314">APICOLTURA</text>
    <text class="label-text brand-name" x="610" y="432">DADO DI SOLE</text>
    <text class="label-text honey-type" x="614" y="538">WILDFLOWER</text>

    <text class="label-text year-caption" x="614" y="640">PRODUCTION YEAR</text>
    <rect class="year-box" x="447" y="652" width="328" height="30"/>

    <g class="origin-flag">
      <rect class="flag-green" x="559" y="737" width="35" height="18"/>
      <rect class="flag-white" x="594" y="737" width="35" height="18"/>
      <rect class="flag-red" x="629" y="737" width="35" height="18"/>
    </g>
  </svg>
</div>
</body>
</html>
```